Professional and creatice Life Coach - Business Card design

I just relaunched my website and now i a need a correspoonding business card for my task as life coach. My website is www.tbalrond.com as reference. The compass is kind of a symbol for my work, as I help people navigate through their challenging phases in life. The business card should be colorful, but not too playful as I also adress business people. So it sould be creative, but professional (also to suport my other business as Management Consultant)

Target Market(s)

People who want to get teir problems resolved, in business, partnership and other personal realms

Industry/Entity Type

Life Coaching

Contact Information for Business Card

Front side should include Name, Phone number, Email, Website and address

Font styles to use
Sans Serif

Colors
add136

Requirements
Must have
• "Mag. Leopold Brantner" -> Name
"Energetische Praxis" -> Jobtitle (describing my profession as life coach)
colours and style should match my website www.tbalrond.com
Nice to have
• a compass as a symbol

```html
<!DOCTYPE html>
<html lang="de">
<head>
<meta charset="utf-8">
<title>Business Card – Leopold Brantner</title>
<link href="https://fonts.googleapis.com/css2?family=Barlow+Semi+Condensed:wght@400;500;700&display=swap" rel="stylesheet">
<style>
  :root {
    --backdrop: #bcbdc0;
    --navy: #0b1626;
    --lime: #add136;
    --white: #ffffff;
    --ink: #0b0b0b;
  }
  html, body {
    margin: 0;
    padding: 0;
    width: 1022px;
    height: 1200px;
    overflow: hidden;
    background: var(--backdrop);
    font-family: "Barlow Semi Condensed", sans-serif;
  }
  .canvas { position: relative; width: 1022px; height: 1200px; }
  .card {
    position: absolute;
    left: 22px;
    width: 977px;
    height: 558px;
    background: var(--navy);
    overflow: hidden;
  }
  .card--front { top: 23px; }
  .card--back { top: 619px; }

  .identity {
    position: absolute;
    right: 363px;
    top: 104px;
    text-align: right;
    line-height: 1;
  }
  .identity__name {
    color: var(--white);
    font-size: 34px;
    font-weight: 400;
    margin: 0;
  }
  .identity__name strong { font-weight: 700; }
  .identity__role {
    color: var(--lime);
    font-size: 27px;
    font-weight: 500;
    margin: 12px 0 0;
    letter-spacing: 0.2px;
  }

  .contact-band {
    position: absolute;
    right: 363px;
    height: 44px;
    background: var(--lime);
    clip-path: polygon(0 0, 100% 0, 100% 100%, 26px 100%);
    display: flex;
    align-items: center;
    color: var(--ink);
    font-size: 27px;
    font-weight: 500;
  }
  .contact-band--address { top: 339px; left: 71px; }
  .contact-band--phone { top: 393px; left: 102px; }
  .contact-band--mail { top: 447px; left: 132px; }
  .contact-band__icon {
    width: 28px;
    height: 28px;
    margin: 0 14px 0 42px;
    flex: none;
  }

  .front-ring {
    position: absolute;
    right: -200px;
    top: 40px;
    width: 470px;
    height: 470px;
  }

  .brand {
    position: absolute;
    left: 0;
    right: 0;
    top: 215px;
    display: flex;
    justify-content: center;
    align-items: center;
    gap: 16px;
    color: var(--lime);
    font-size: 48px;
    font-weight: 700;
    letter-spacing: 4px;
  }
  .brand__dot {
    width: 34px;
    height: 34px;
    border: 5px solid var(--lime);
    border-radius: 50%;
    box-sizing: border-box;
  }
  .website {
    position: absolute;
    left: 0;
    right: 0;
    top: 436px;
    text-align: center;
    color: var(--lime);
    font-size: 27px;
    font-weight: 400;
    letter-spacing: 12.5px;
  }
</style>
</head>
<body>
<div class="canvas">
  <section class="card card--front">
    <div class="identity">
      <h1 class="identity__name">Mag. <strong>Leopold Brantner</strong></h1>
      <p class="identity__role">ENERGETISCHE PRAXIS</p>
    </div>

    <div class="contact-band contact-band--address">
      <svg class="contact-band__icon" viewBox="0 0 28 28" aria-hidden="true">
        <circle cx="14" cy="14" r="14" fill="var(--ink)"/>
        <path d="M7 14 L14 7.5 L21 14 M9.5 12 V20.5 H18.5 V12" fill="none" stroke="var(--white)" stroke-width="1.8" stroke-linejoin="round"/>
        <rect x="12.5" y="15.5" width="3" height="5" fill="var(--white)"/>
      </svg>
      <span>Lindenweg 12, 5020 Salzburg, Österreich</span>
    </div>
    <div class="contact-band contact-band--phone">
      <svg class="contact-band__icon" viewBox="0 0 28 28" aria-hidden="true">
        <circle cx="14" cy="14" r="14" fill="var(--ink)"/>
        <path d="M9 7.5 L11.5 7.5 L12.5 11 L10.8 12.3 C11.8 14.5 13.5 16.2 15.7 17.2 L17 15.5 L20.5 16.5 L20.5 19 C20.5 19.8 19.8 20.5 19 20.5 C13 20.2 7.8 15 7.5 9 C7.5 8.2 8.2 7.5 9 7.5 Z" fill="none" stroke="var(--white)" stroke-width="1.6" stroke-linejoin="round"/>
      </svg>
      <span>+43 660 4817392</span>
    </div>
    <div class="contact-band contact-band--mail">
      <svg class="contact-band__icon" viewBox="0 0 28 28" aria-hidden="true">
        <circle cx="14" cy="14" r="14" fill="var(--ink)"/>
        <rect x="7.5" y="9.5" width="13" height="9" fill="none" stroke="var(--white)" stroke-width="1.6"/>
        <path d="M7.5 9.5 L14 15 L20.5 9.5" fill="none" stroke="var(--white)" stroke-width="1.6"/>
      </svg>
      <span>leopold@tbalrond.co</span>
    </div>

    <svg class="front-ring" viewBox="0 0 470 470" aria-hidden="true">
      <circle cx="235" cy="235" r="222" fill="none" stroke="var(--lime)" stroke-width="9" opacity="0.85"/>
    </svg>
  </section>

  <section class="card card--back">
    <div class="brand">
      <span class="brand__dot"></span>
      <span>TBALROND</span>
    </div>
    <p class="website">www.tbalrond.com</p>
  </section>
</div>
</body>
</html>
```